Harwick Legal

To update and modernize current business card appearance. Marta's business is based in Melbourne with 4 other lawyers in the firm. Marta travels to the Pilbara in Western Australia approximately 1 week a month as part of the firms legal work. She consults with clients in Newman, Tom Price and Port Hedland. The lawyers work mostly from a home office, apart from court appearances. They have a virtual office in Melbourne city, and use facilities in 3 or 4 other locations around Melbourne. It is important the client's think this is a conventional law firm with a permanent office. Our business structure is a difficult concept for them to grasp. The business has been operational for 3 years, growing from 1 lawyer to 4 lawyers during that time. Our website is www.Harwicklegal.example.au and is currently being upgraded as we are not happy with its content. The logo is currently orange and dark grey but the orange is a difficult colour to reproduce and often turns out "poo" brown when documents are printed. We need clients to know we are user friendly and caring - and not head up our rears ends as some lawyers appear to be.
Updates

Thank you for the feedback so far. 1. Some of the designs have too much black (We prefer darker grey & not too much.) 2. Happy for designers to play around with different colours & logo design. What we're after is a modern look and business card that people say "wow" when they pick it up.

Industry/Entity Type

Business

```html
<!DOCTYPE html>
<html lang="en">
<head>
<meta charset="utf-8">
<title>Harwick Legal – Business Cards</title>
<link rel="stylesheet" href="https://fonts.googleapis.com/css2?family=Cormorant+SC:wght@500;600&family=Open+Sans:wght@400;700&display=swap">
<style>
  :root {
    --bg: #d9d6d1;
    --card-dark: #4a4a4b;
    --card-light: #e9e9e8;
    --band: #4a4a4b;
    --accent: #c9442c;
    --ink: #4a4a4b;
    --ink-soft: #5c5c5c;
    --on-dark: #f1f1f1;
    --serif: "Cormorant SC", Georgia, serif;
    --sans: "Open Sans", Arial, sans-serif;
  }
  * { box-sizing: border-box; margin: 0; padding: 0; }
  html, body { width: 1200px; height: 900px; overflow: hidden; }
  body {
    background: var(--bg);
    position: relative;
    font-family: var(--sans);
  }
  .card {
    position: absolute;
    width: 540px;
    height: 309px;
    border-radius: 3px;
    box-shadow: 0 10px 24px rgba(0,0,0,.22);
    overflow: hidden;
  }

  /* Back of card */
  .card-back {
    left: 330px; top: 80px;
    background: var(--card-dark);
    color: var(--on-dark);
    font-family: var(--serif);
  }
  .card-back .tagline {
    position: absolute; left: 34px; top: 28px;
    font-size: 21px; letter-spacing: 1px;
  }
  .card-back .rule {
    position: absolute; height: 2px; background: var(--accent);
  }
  .card-back .rule-top { left: 34px; top: 64px; width: 300px; }
  .card-back .rule-bottom { left: 200px; top: 240px; width: 306px; }
  .brand-back {
    position: absolute; left: 34px; top: 140px;
    display: flex; align-items: center; gap: 10px;
  }
  .brand-dot { width: 18px; height: 18px; border-radius: 50%; background: var(--accent); }
  .brand-back .brand-name {
    font-family: var(--serif); font-weight: 600; font-size: 26px; color: var(--on-dark);
  }
  .services {
    position: absolute; left: 292px; top: 86px;
    list-style: none; font-size: 17px; line-height: 1.25;
  }
  .services .area { font-weight: 600; }
  .services .sub { padding-left: 16px; }
  .services .area::before { content: "• "; }
  .card-back .email {
    position: absolute; right: 34px; top: 254px;
    font-size: 18px; letter-spacing: .3px;
  }

  /* Front of card */
  .card-front {
    left: 330px; top: 500px;
    background: var(--card-light);
    color: var(--ink);
  }
  .brand-front {
    position: absolute; left: 36px; top: 98px;
    display: flex; align-items: center; gap: 10px;
  }
  .brand-front .brand-name {
    font-family: var(--sans); font-weight: 700; font-size: 26px; color: var(--ink);
  }
  .person { position: absolute; left: 286px; top: 32px; }
  .person .name { font-weight: 700; font-size: 16px; letter-spacing: .3px; }
  .person .quals, .person .role { font-size: 13px; color: var(--ink-soft); }
  .person .role { font-size: 15px; }
  .contact {
    position: absolute; left: 286px; top: 114px;
    list-style: none; font-size: 13px; line-height: 1.45; color: var(--ink-soft);
  }
  .contact .key { color: var(--accent); display: inline-block; width: 14px; }
  .location-band {
    position: absolute; left: 0; right: 0; bottom: 0; height: 84px;
    background: var(--band); color: var(--on-dark);
    text-align: right; padding: 16px 34px 0 0;
    font-size: 17px; line-height: 1.3;
  }
</style>
</head>
<body>

<section class="card card-back" aria-label="Business card back">
  <p class="tagline">Experience • Support • Solutions</p>
  <div class="rule rule-top"></div>
  <div class="brand-back">
    <span class="brand-dot"></span>
    <span class="brand-name">Harwick Legal</span>
  </div>
  <ul class="services">
    <li class="area">Family Law •</li>
    <li class="sub">Collaborative Practice</li>
    <li class="sub">Mediation &amp; Negotiation</li>
    <li class="sub">Intervention Orders</li>
    <li class="area">Criminal Law •</li>
  </ul>
  <div class="rule rule-bottom"></div>
  <p class="email">info@harwicklegal.example.au</p>
</section>

<section class="card card-front" aria-label="Business card front">
  <div class="brand-front">
    <span class="brand-dot"></span>
    <span class="brand-name">Harwick Legal</span>
  </div>
  <div class="person">
    <p class="name">J. MARTA QUINLAN</p>
    <p class="quals">LLB (Hons) - Accredited Mediator</p>
    <p class="role">Principal Solicitor</p>
  </div>
  <ul class="contact">
    <li><span class="key">T</span>1300 Harwick (427 942)</li>
    <li><span class="key">M</span>0400 118 274</li>
    <li><span class="key">E</span>marta.quinlan@harwicklegal.example.au</li>
  </ul>
  <div class="location-band">
    <p>MELBOURNE</p>
    <p>Eastern and Bayside Suburbs</p>
  </div>
</section>

</body>
</html>
```